Natural Skincare brand needs new labels!

We are a natural and organic skin care brand based in the united states. We are looking for unique product label designs that will help our brand stand out. We want the labels to look elegant and natural, but also incorporate some color. We want a design aspect like a line drawing on the labels, see examples. Please refer to our website to see our current labels and to get more of a feel of who we are. Our logo is included. We are looking for 5 labels for 5 different Products.
1. Body butter: 1.5"x9" rectangle wrap around 12oz jar with black lid
2. Eczema Salve: 1.5" circle silver metal tin
3. Glow Serum: 1.5"x3" rectangle Blue Dropper Bottle with black top
4. Mineral Mist: 1.5"x3" clear glass sprayer bottle (want clear label)
website: www.venalubotanics.com
Instagram: @venalubotanics

```html
<!DOCTYPE html>
<html lang="en">
<head>
<meta charset="utf-8">
<title>Venalu Botanics — Glow Serum &amp; Mineral Mist Labels</title>
<link rel="stylesheet" href="https://fonts.googleapis.com/css2?family=Barlow:wght@400;500;600&display=swap">
<style>
  :root {
    --page-bg: #ebebeb;
    --label-white: #ffffff;
    --label-mist: #f5f5f6;
    --serum-band: #5b5a9f;
    --serum-accent: #8b8dc9;
    --serum-blob: #bfbedd;
    --mist-band: #a4bfe4;
    --mist-blob: #d3deef;
    --mist-accent: #6a7db8;
    --brand-rose: #c4907f;
    --brand-grey: #8c8586;
    --ink: #2f2f33;
    --sprig: #cfcfd3;
  }
  * { margin: 0; padding: 0; box-sizing: border-box; }
  html, body { width: 1200px; height: 1082px; overflow: hidden; }
  body {
    background: var(--page-bg);
    font-family: "Barlow", Arial, sans-serif;
    color: var(--ink);
    position: relative;
  }
  .label {
    position: absolute;
    top: 150px;
    width: 340px;
    height: 676px;
    overflow: hidden;
    box-shadow: 0 2px 10px rgba(0,0,0,0.06);
  }
  .label--serum { left: 200px; background: var(--label-white); }
  .label--mist { left: 660px; background: var(--label-mist); }
  .label__shapes { position: absolute; inset: 0; width: 100%; height: 100%; }
  .brand {
    position: absolute;
    left: 0; right: 0;
    top: 96px;
    display: flex;
    align-items: center;
    justify-content: center;
    gap: 10px;
    font-weight: 500;
    font-size: 30px;
    letter-spacing: 0.04em;
    line-height: 1;
  }
  .brand__dot { width: 18px; height: 18px; border-radius: 50%; flex: none; }
  .label--serum .brand { color: var(--brand-rose); }
  .label--serum .brand__dot { background: var(--brand-rose); }
  .label--mist .brand { color: var(--brand-grey); }
  .label--mist .brand__dot { background: var(--brand-grey); }
  .band {
    position: absolute;
    left: 0; right: 0;
    top: 220px;
    height: 73px;
    display: flex;
    align-items: center;
    justify-content: center;
    color: #fff;
    font-size: 27px;
    font-weight: 500;
    letter-spacing: 0.3em;
    padding-left: 0.3em;
  }
  .label--serum .band { background: var(--serum-band); }
  .label--mist .band { background: var(--mist-band); }
  .serum-claim {
    position: absolute;
    left: 0; right: 0;
    top: 314px;
    text-align: center;
    color: var(--serum-accent);
    font-size: 20px;
    line-height: 26px;
    letter-spacing: 0.06em;
  }
  .ingredients { position: absolute; left: 30px; top: 460px; }
  .ingredients__title { font-weight: 600; font-size: 18px; margin-bottom: 6px; }
  .ingredients__text { font-size: 19px; line-height: 25px; }
  .size { position: absolute; font-size: 19px; font-weight: 500; }
  .label--serum .size { left: 28px; top: 606px; }
  .label--mist .size { left: 20px; top: 640px; z-index: 2; }
  .sprig { position: absolute; }
  .label--serum .sprig--main { right: 0; top: 380px; width: 135px; height: 296px; }
  .label--mist .sprig--main { right: 0; top: 300px; width: 150px; height: 376px; }
  .label--mist .sprig--side { left: 0; top: 515px; width: 80px; height: 161px; }
  .sprig { background: linear-gradient(160deg, rgba(207,207,211,0.0), rgba(190,190,196,0.45)); }
  .mist-benefit {
    position: absolute;
    left: 18px;
    top: 510px;
    transform-origin: left top;
    transform: rotate(-90deg);
    color: var(--mist-accent);
    font-size: 35px;
    letter-spacing: 0.12em;
    white-space: nowrap;
  }
  .mist-stone {
    position: absolute;
    left: 100px;
    top: 636px;
    color: #6a8fc0;
    font-size: 25px;
    font-weight: 500;
    letter-spacing: 0.1em;
    z-index: 2;
  }
  .note {
    position: absolute;
    left: 64px;
    top: 990px;
    font-size: 30px;
    font-weight: 500;
  }
</style>
</head>
<body>

<section class="label label--serum">
  <svg class="label__shapes" viewBox="0 0 340 676" aria-hidden="true">
    <path d="M215 0 H340 V70 A110 110 0 0 1 215 0 Z" fill="var(--serum-blob)"/>
    <path d="M135 0 C190 40 260 60 340 70" fill="none" stroke="#ececf0" stroke-width="1.5"/>
    <path d="M40 676 C90 640 200 625 340 640 V676 Z" fill="var(--serum-blob)"/>
    <path d="M0 660 C70 620 180 600 300 612" fill="none" stroke="#ececf0" stroke-width="1.5"/>
  </svg>
  <div class="brand"><span class="brand__dot"></span>Venalu Botanics</div>
  <div class="band">GLOW SERUM</div>
  <p class="serum-claim">Manjishta + Safflower<br>GLOW + EVEN SKIN TONE</p>
  <div class="ingredients">
    <p class="ingredients__title">Ingredients</p>
    <p class="ingredients__text">Lorem ipsum dolor sit<br>amet, consectetuer</p>
  </div>
  <p class="size">2 oz</p>
  <div class="sprig sprig--main" role="img" aria-label="Grey line drawing of leafy botanical sprigs"></div>
</section>

<section class="label label--mist">
  <svg class="label__shapes" viewBox="0 0 340 676" aria-hidden="true">
    <path d="M0 0 H180 C140 30 80 50 0 38 Z" fill="var(--mist-blob)"/>
    <path d="M0 52 C60 62 130 40 180 0" fill="none" stroke="#e4e4e8" stroke-width="1.5"/>
    <path d="M30 676 C70 630 200 600 340 640 V676 Z" fill="var(--mist-blob)"/>
  </svg>
  <div class="brand"><span class="brand__dot"></span>Venalu Botanics</div>
  <div class="band">MINERAL MIST</div>
  <p class="mist-benefit">HEALING</p>
  <div class="sprig sprig--main" role="img" aria-label="Light grey line drawing of leafy botanical sprigs"></div>
  <div class="sprig sprig--side" role="img" aria-label="Small grey line drawing of a botanical sprig"></div>
  <p class="size">4 oz</p>
  <p class="mist-stone">Clear Quarz</p>
</section>

<p class="note">Suggest: use matte labels.</p>

</body>
</html>
```